BRIVON - Business Card Design Project

We need a business card design for a consultant company called BRIVON, LLC. (stands for Bright Retail Inventory Venture Operations Network). The company provides Information Technology solutions, custom applications, services for financial and supply chain worldwide and focuses on business IT process improvements and all the steps leading to the procurement or integrating of any Enterprise related systems.

Industry/Entity Type

Financial

Requirements
Must have
• - In the submitted proposed version you should have one variant with black background and one with white.
The designer should show the shadow element of the company name in binary code (010000100101001001001001010101100100111101001110). It can be in one line or split in two

In your example please use the following info
Peter Dorne
Principal Consultant
pdorne@brivonhq.net
+1 (555) 014 - 2298

Please keep in mind that the design should have some spaces to add the second phone and/or web site name
Nice to have
• Since this IT company and is working closely with Accounting and Logistics Application you can add some elements (contour only) of these types of the bussines as well (for example some $ or euro sign or truck or warehouse element)
Should not have
• Don’t use any extra color that is not in the company color logo pattern

```html
<!DOCTYPE html>
<html lang="en">
<head>
<meta charset="utf-8">
<title>BRIVON – Business Card</title>
<link href="https://fonts.googleapis.com/css2?family=Michroma&family=Jura:wght@500&display=swap" rel="stylesheet">
<style>
  :root {
    --backdrop: #b9b9b9;
    --ink-black: #161616;
    --paper-white: #f4f4f2;
    --band-blue-dark: #1b6f93;
    --band-blue-light: #2fa6d4;
    --accent-green: #4a9a2a;
    --accent-green-light: #8cc63f;
    --accent-orange: #e0591c;
    --accent-yellow: #f4a81d;
    --accent-red: #c8321e;
    --text-dark: #222;
    --text-light: #ffffff;
    --binary-shadow: rgba(255,255,255,.16);
  }
  * { box-sizing: border-box; margin: 0; padding: 0; }
  html, body { width: 1200px; height: 720px; overflow: hidden; }
  body {
    background: var(--backdrop);
    display: flex;
    align-items: center;
    justify-content: center;
    gap: 32px;
  }
  .card {
    position: relative;
    width: 560px;
    height: 320px;
    overflow: hidden;
    box-shadow: 0 8px 22px rgba(0,0,0,.28);
  }

  /* ---------- front ---------- */
  .card--front { background: var(--paper-white); }
  .front__top {
    position: absolute; left: 0; top: 0; width: 100%; height: 96px;
    background: var(--ink-black);
  }
  .front__side {
    position: absolute; right: 0; top: 96px; width: 170px; height: 56px;
    background: var(--ink-black);
  }
  .front__band {
    position: absolute; left: 0; top: 96px; width: 390px; height: 56px;
    background: linear-gradient(90deg, var(--band-blue-light), var(--band-blue-dark));
    display: flex; align-items: center; padding-left: 26px;
    color: var(--text-light);
  }
  .front__rule {
    position: absolute; left: 0; top: 158px; width: 395px; height: 2px;
    background: var(--band-blue-dark);
  }
  .person__name {
    font-family: "Michroma", sans-serif; font-size: 19px; letter-spacing: .5px;
  }
  .person__divider {
    width: 1px; height: 30px; background: rgba(255,255,255,.8); margin: 0 12px;
  }
  .person__role { font-family: "Jura", sans-serif; font-size: 11px; }

  .brand {
    position: absolute; display: flex; align-items: center; gap: 12px;
    color: var(--text-light);
  }
  .brand__dot {
    width: 30px; height: 30px; border-radius: 50%;
    background: var(--band-blue-light); flex: none;
  }
  .brand__name {
    position: relative;
    font-family: "Michroma", sans-serif; font-size: 34px; letter-spacing: 2px; line-height: 1;
  }
  .brand__tagline {
    font-family: "Jura", sans-serif; font-size: 8.5px; letter-spacing: .2px; margin-top: 4px;
  }
  .card--front .brand { right: 26px; top: 38px; }

  .binary-shadow {
    position: absolute;
    font-family: "Jura", sans-serif;
    color: var(--binary-shadow);
    letter-spacing: 1.5px;
    line-height: 1.35;
    white-space: nowrap;
  }
  .card--front .binary-shadow { left: 26px; top: 30px; font-size: 10px; }

  .accent-blocks { position: absolute; right: 18px; top: 140px; }

  .contact {
    position: absolute; left: 232px; top: 186px;
    list-style: none; font-family: "Jura", sans-serif; font-size: 15px; color: var(--text-dark);
  }
  .contact__item { display: flex; align-items: center; gap: 9px; height: 21px; white-space: nowrap; }
  .contact__icon { width: 13px; height: 13px; fill: #333; flex: none; }

  /* ---------- back ---------- */
  .card--back { background: var(--ink-black); }
  .card--back .brand { left: 40px; top: 48px; }
  .card--back .brand__name { font-size: 40px; }
  .card--back .binary-shadow { left: 84px; top: 108px; font-size: 12px; }
  .back__decoration {
    position: absolute; right: 0; top: 150px; width: 300px; height: 170px;
    background:
      linear-gradient(90deg, var(--ink-black), rgba(22,22,22,0) 60%),
      linear-gradient(160deg, rgba(47,166,212,.35), rgba(140,198,63,.3) 50%, rgba(224,89,28,.35));
  }
</style>
</head>
<body>

  <section class="card card--front">
    <div class="front__top"></div>
    <div class="front__side"></div>
    <div class="binary-shadow" aria-hidden="true">010000100101001001001001<br>010101100100111101001110</div>
    <div class="front__band">
      <span class="person__name">Peter Dorne</span>
      <span class="person__divider"></span>
      <span class="person__role">Principal Consultant</span>
    </div>
    <div class="front__rule"></div>

    <div class="brand">
      <span class="brand__dot"></span>
      <div>
        <div class="brand__name">BRIVON</div>
        <div class="brand__tagline">Bright Retail Inventory Venture Operations Network</div>
      </div>
    </div>

    <svg class="accent-blocks" width="140" height="48" viewBox="0 0 140 48" aria-hidden="true">
      <defs>
        <linearGradient id="greenBlock" x1="0" y1="0" x2="1" y2="1">
          <stop offset="0" stop-color="#8cc63f"/>
          <stop offset="1" stop-color="#4a9a2a"/>
        </linearGradient>
        <linearGradient id="orangeBlock" x1="0" y1="0" x2="1" y2="1">
          <stop offset="0" stop-color="#f4a81d"/>
          <stop offset="1" stop-color="#e0591c"/>
        </linearGradient>
      </defs>
      <polygon points="10,0 66,0 58,36 2,36" fill="url(#greenBlock)"/>
      <polygon points="80,0 136,0 128,36 72,36" fill="url(#orangeBlock)"/>
      <rect x="0" y="42" width="58" height="2" fill="#4a9a2a"/>
      <rect x="70" y="42" width="60" height="2" fill="#c8321e"/>
    </svg>

    <ul class="contact">
      <li class="contact__item">
        <svg class="contact__icon" viewBox="0 0 16 16"><path d="M8 1 1 8h2v7h4v-4h2v4h4V8h2z"/></svg>
        Street 0, City Town, Larkfield, Norvania
      </li>
      <li class="contact__item">
        <svg class="contact__icon" viewBox="0 0 16 16"><path d="M4 0h8v16H4zM5.5 2v10h5V2zM7 13.5h2v1H7z" fill-rule="evenodd"/></svg>
        +1 (555) 014 - 2298
      </li>
      <li class="contact__item">
        <svg class="contact__icon" viewBox="0 0 16 16"><path d="M3 1h3l1.5 4-2 1.5a9 9 0 0 0 4 4L11 8.5l4 1.5v3c0 1-1 2-2 2A12 12 0 0 1 1 3c0-1 1-2 2-2z"/></svg>
        +1 (555) 014 - 2299
      </li>
      <li class="contact__item">
        <svg class="contact__icon" viewBox="0 0 16 16"><path d="M1 3h14v10H1zM2.5 4.5v.6L8 9l5.5-3.9v-.6zm0 2.4v4.6h11V6.9L8 10.8z" fill-rule="evenodd"/></svg>
        pdorne@brivonhq.net
      </li>
      <li class="contact__item">
        <svg class="contact__icon" viewBox="0 0 16 16"><path d="M8 1a7 7 0 1 0 0 14A7 7 0 0 0 8 1zm0 1.5a5.5 5.5 0 1 1 0 11 5.5 5.5 0 0 1 0-11zM2.5 8h11M8 2.5v11" fill-rule="evenodd"/></svg>
        www.brivonhq.com
      </li>
    </ul>
  </section>

  <section class="card card--back">
    <div class="back__decoration" role="img" aria-label="Large decorative line motif in blue, green and orange"></div>
    <div class="binary-shadow" aria-hidden="true">010000100101001001001001<br>010101100100111101001110</div>
    <div class="brand">
      <span class="brand__dot"></span>
      <div class="brand__name">BRIVON</div>
    </div>
  </section>

</body>
</html>
```